Veltrona Cabinets Letter Head and Email Signature

Hi
I would love a design package for a letterhead, email signature, even update my business card if you like if you can come up with a great idea for my new high end cabinet shop. Veltrona Cabinets brings timeless craftsmanship to modern interiors, specializing in high end, custom cabinetry designed for architects and interior designers.

Target Market(s)

high end, luxury market

Industry/Entity Type

cabinet making

Requirements
Must have
• my colours of logo as the theme

```html
<!DOCTYPE html>
<html lang="en">
<head>
<meta charset="utf-8">
<title>Veltrona Cabinets – Letterhead and Email Signature</title>
<link href="https://fonts.googleapis.com/css2?family=Arimo:wght@400&family=Tinos&display=swap" rel="stylesheet">
<style>
  :root {
    --backdrop: #d3d4d6;
    --ink: #000000;
    --paper: #ffffff;
    --brand-green: #4a7c4a;
    --text-dark: #111111;
  }
  * { margin: 0; padding: 0; box-sizing: border-box; }
  html, body { width: 1200px; height: 829px; overflow: hidden; background: var(--backdrop); }
  .canvas { position: relative; width: 1200px; height: 829px; }

  .letterhead {
    position: absolute; left: 68px; top: 98px; width: 442px; height: 624px;
    background: var(--paper); box-shadow: 0 4px 18px rgba(0,0,0,.22);
  }
  .letterhead-header {
    position: absolute; left: 0; top: 0; width: 100%; height: 86px; background: var(--ink);
    border-bottom: 3px solid var(--brand-green);
  }
  .brand-name {
    position: absolute; font-family: "Arimo", Arial, sans-serif; font-weight: 400;
    color: var(--brand-green); line-height: 1; white-space: nowrap;
  }
  .brand-name .brand-square {
    display: inline-block; border: 2px solid var(--brand-green); vertical-align: middle;
  }
  .brand-name .word-top { display: block; }
  .brand-name .word-bottom { display: block; }

  .letterhead .brand-name { left: 11px; top: 25px; }
  .letterhead .brand-square { width: 22px; height: 22px; position: absolute; left: 0; top: 10px; }
  .letterhead .word-top { font-size: 24px; margin-left: 34px; }
  .letterhead .word-bottom { font-size: 11px; letter-spacing: 4.2px; margin-left: 35px; margin-top: 4px; }

  .divider { position: absolute; width: 1px; background: #6a6a6a; }
  .contact-block {
    position: absolute; font-family: "Tinos", "Times New Roman", serif; color: var(--paper);
    white-space: nowrap;
  }
  .contact-line { display: flex; align-items: center; }
  .contact-line svg { flex: none; fill: var(--brand-green); }

  .letterhead .divider-one { left: 176px; top: 32px; height: 30px; }
  .letterhead .divider-two { left: 325px; top: 27px; height: 30px; }
  .letterhead .contact-phone-mail { left: 190px; top: 35px; font-size: 8.4px; line-height: 11.5px; }
  .letterhead .contact-web-address { left: 334px; top: 26px; font-size: 8.4px; line-height: 10.4px; }
  .letterhead .contact-line svg { width: 7px; height: 7px; margin-right: 6px; }
  .letterhead .address-gap { margin-top: 4px; }
  .letterhead .indent { padding-left: 13px; }

  .letter-body {
    position: absolute; left: 68px; top: 206px; width: 309px;
    font-family: "Arimo", Arial, sans-serif; font-size: 8.6px; line-height: 10px;
    color: var(--text-dark); text-align: justify;
  }
  .letter-body p { margin-bottom: 0; }
  .letter-body p + p { margin-top: 21px; }

  .letterhead-footer { position: absolute; left: 0; bottom: 0; width: 442px; height: 19px; }

  .email-signature {
    position: absolute; left: 559px; top: 420px; width: 575px; height: 168px;
    background: var(--paper); box-shadow: 0 4px 14px rgba(0,0,0,.2);
  }
  .signature-panel { position: absolute; left: 0; top: 0; width: 100%; height: 150px; background: var(--ink); }
  .email-signature .brand-name { left: 36px; top: 62px; }
  .email-signature .brand-square { width: 28px; height: 28px; position: absolute; left: 0; top: 12px; }
  .email-signature .word-top { font-size: 30px; margin-left: 43px; }
  .email-signature .word-bottom { font-size: 14px; letter-spacing: 5.6px; margin-left: 44px; margin-top: 5px; }
  .email-signature .divider-one { left: 235px; top: 69px; height: 38px; }
  .email-signature .divider-two { left: 417px; top: 63px; height: 38px; }
  .email-signature .contact-phone-mail { left: 252px; top: 72px; font-size: 11px; line-height: 15px; }
  .email-signature .contact-web-address { left: 427px; top: 62px; font-size: 11px; line-height: 12.6px; }
  .email-signature .contact-line svg { width: 9px; height: 9px; margin-right: 7px; }
  .email-signature .address-gap { margin-top: 6px; }
  .email-signature .indent { padding-left: 16px; }
  .signature-footer { position: absolute; left: 0; top: 147px; width: 575px; height: 21px; }
</style>
</head>
<body>
<div class="canvas">

  <section class="letterhead">
    <header class="letterhead-header">
      <div class="brand-name">
        <span class="brand-square"></span>
        <span class="word-top">Veltrona</span>
        <span class="word-bottom">CABINETS</span>
      </div>
      <span class="divider divider-one"></span>
      <div class="contact-block contact-phone-mail">
        <div class="contact-line">
          <svg viewBox="0 0 10 10"><path d="M2 0.5 L3.6 2.6 L2.7 3.6 Q3.8 5.8 6.2 7.2 L7.3 6.3 L9.5 8 L8.3 9.5 Q2.5 8.5 0.5 1.8 Z"/></svg>
          <span>0491570156</span>
        </div>
        <div class="contact-line">
          <svg viewBox="0 0 10 10"><path d="M0.5 2 H9.5 V8.5 H0.5 Z M1 2.4 L5 5.6 L9 2.4" stroke="#000" stroke-width="0.8"/></svg>
          <span>info@veltronacabinets.com.au</span>
        </div>
      </div>
      <span class="divider divider-two"></span>
      <div class="contact-block contact-web-address">
        <div class="contact-line">
          <svg viewBox="0 0 10 10"><circle cx="5" cy="5" r="4.5"/><path d="M2.5 3 Q4 4 3.5 6 M6 2 Q5.5 4 7.5 5" stroke="#000" stroke-width="0.8" fill="none"/></svg>
          <span>www.websitename.com</span>
        </div>
        <div class="contact-line address-gap">
          <svg viewBox="0 0 10 10"><path d="M5 0.5 A3.3 3.3 0 0 1 8.3 3.8 Q8.3 6 5 9.5 Q1.7 6 1.7 3.8 A3.3 3.3 0 0 1 5 0.5 Z M5 2.6 A1.2 1.2 0 1 0 5 5 A1.2 1.2 0 1 0 5 2.6 Z"/></svg>
          <span>421, Address line here</span>
        </div>
        <div class="contact-line indent">Country Name, 45452</div>
      </div>
    </header>

    <div class="letter-body">
      <p>Lorem ipsum dolor sit amet, consectetur adipiscing elit. Donec fringilla neque euismod volutpat cursus. Vestibulum ac pretium orci, consequat elementum velit. Etiam bibendum purus ac augue finibus volutpat. Vestibulum justo nisl</p>
      <p>Lorem ipsum dolor sit amet, consectetur adipiscing elit. Donec fringilla neque euismod volutpat cursus. Vestibulum ac pretium orci, consequat elementum velit. Etiam bibendum purus ac augue finibus volutpat. Vestibulum justo nisl, gravida aliquet sollicitudin ut, finibus vitae mi. Praesent aliquet scelerisque blandit. Sed id varius lacus, id tristique sem. Fusce et lobortis leo. Aliquam mollis pellentesque magna, condimentum ullamcorper ex ullamcorper non. Morbi ultricies nunc eu tellus dignissim, eget venenatis dolor ullamcorper. Etiam dolor eros, iaculis at ultricies nec, volutpat nec orci. Vivamus tincidunt rutrum sapien, ac porttitor mauris tristique nec.</p>
      <p>Lorem ipsum dolor sit amet, consectetur adipiscing elit. Donec fringilla neque euismod volutpat cursus. Vestibulum ac pretium orci, consequat elementum velit. Etiam bibendum purus ac augue finibus volutpat. Vestibulum justo nisl, gravida aliquet sollicitudin ut, finibus vitae mi. Praesent aliquet scelerisque blandit. Sed id varius lacus, id tristique sem. Fusce et lobortis leo. Aliquam mollis pellentesque magna, condimentum ullamcorper ex ullamcorper non. Morbi ultricies nunc eu tellus dignissim, eget venenatis dolor ullamcorper. Etiam dolor eros, iaculis at ultricies nec, volutpat nec orci. Vivamus tincidunt rutrum sapien, ac porttitor mauris tristique nec.</p>
      <p>Lorem ipsum dolor sit amet, consectetur adipiscing elit. Donec fringilla neque euismod volutpat cursus. Vestibulum ac pretium orci, consequat elementum velit. Etiam bibendum purus ac augue finibus volutpat. Vestibulum justo nisl</p>
    </div>

    <svg class="letterhead-footer" viewBox="0 0 442 19" preserveAspectRatio="none">
      <polygon points="0,2 201,2 218,17.5 0,18" fill="var(--ink)"/>
      <polygon points="209,1 442,0 442,16.5 227,17" fill="var(--brand-green)"/>
    </svg>
  </section>

  <section class="email-signature">
    <div class="signature-panel">
      <div class="brand-name">
        <span class="brand-square"></span>
        <span class="word-top">Veltrona</span>
        <span class="word-bottom">CABINETS</span>
      </div>
      <span class="divider divider-one"></span>
      <div class="contact-block contact-phone-mail">
        <div class="contact-line">
          <svg viewBox="0 0 10 10"><path d="M2 0.5 L3.6 2.6 L2.7 3.6 Q3.8 5.8 6.2 7.2 L7.3 6.3 L9.5 8 L8.3 9.5 Q2.5 8.5 0.5 1.8 Z"/></svg>
          <span>0491570156</span>
        </div>
        <div class="contact-line">
          <svg viewBox="0 0 10 10"><path d="M0.5 2 H9.5 V8.5 H0.5 Z M1 2.4 L5 5.6 L9 2.4" stroke="#000" stroke-width="0.8"/></svg>
          <span>info@veltronacabinets.com.au</span>
        </div>
      </div>
      <span class="divider divider-two"></span>
      <div class="contact-block contact-web-address">
        <div class="contact-line">
          <svg viewBox="0 0 10 10"><circle cx="5" cy="5" r="4.5"/><path d="M2.5 3 Q4 4 3.5 6 M6 2 Q5.5 4 7.5 5" stroke="#000" stroke-width="0.8" fill="none"/></svg>
          <span>www.websitename.com</span>
        </div>
        <div class="contact-line address-gap">
          <svg viewBox="0 0 10 10"><path d="M5 0.5 A3.3 3.3 0 0 1 8.3 3.8 Q8.3 6 5 9.5 Q1.7 6 1.7 3.8 A3.3 3.3 0 0 1 5 0.5 Z M5 2.6 A1.2 1.2 0 1 0 5 5 A1.2 1.2 0 1 0 5 2.6 Z"/></svg>
          <span>421, Address line here</span>
        </div>
        <div class="contact-line indent">Country Name, 45452</div>
      </div>
    </div>
    <svg class="signature-footer" viewBox="0 0 575 21" preserveAspectRatio="none">
      <polygon points="260,3 272,3 294,21 283,21" fill="var(--ink)"/>
      <polygon points="270,3 575,0 575,21 294,21" fill="var(--brand-green)"/>
    </svg>
  </section>

</div>
</body>
</html>
```